Natural and organic skincare brand needs label design!

I need labels designed for my natural and organic skincare brand lumavale. The front of the bottles must contain the logo (image attached) and the following words: Formulated by a Naturopath; Anti-aging therapy; Organic Facial Oil; with CoEnzyme Q10 and Rosehip Seed Oil; 100ml e3.38fl.oz. Colours I would like used include black/white/grey/silver and aqua. I also like the grey woodgrain used on my draft website (check out www.lumavale-skin.com.au). The logo should be silver foil (shiny).The final design should be simple and communicate nature and sophistication. Some designs I like are found in the attachments. I intend to use black or white bottles.

Target Market(s)

women aged 30-50 interested in natural products

Industry/Entity Type

Skin Care Product

Font styles to use
Serif
Sans Serif
Decorative
Script
Other font styles liked:
• Any

Requirements
Must have
• Dimensions: 62mm (w) x 75mm (H) (front label only)
• Must contain the logo (image attached). The logo should be silver foil (shiny). and the following words are to be included on the label:
• Formulated by a Naturopath;
• Anti-aging Therapy;
• Organic Facial Oil;
• with CoEnzyme Q10 and Rosehip Seed Oil;
• 100ml e3.38fl.oz.
Nice to have
• Colours I would like used include black/white/grey/silver and aqua (turquoise). But I am also open to suggestion. I also like the grey woodgrain used on my draft website (check out www.lumavale-skin.com.au)

```html
<!DOCTYPE html>
<html lang="en">
<head>
<meta charset="utf-8">
<title>lumavale – Organic Facial Oil front label</title>
<link rel="stylesheet" href="https://fonts.googleapis.com/css2?family=Tinos:wght@400&family=Josefin+Sans:wght@300&display=swap">
<style>
  :root {
    --backdrop: #201e1f;
    --label: #ffffff;
    --slate: #535d6b;
    --leaf-mid: #c3c6cd;
    --leaf-pale: #e6e7e9;
    --copy-grey: #77777b;
    --copy-dark: #1f1f20;
  }
  html, body {
    margin: 0;
    padding: 0;
    width: 1200px;
    height: 1200px;
    overflow: hidden;
    background: var(--backdrop);
  }
  .label {
    position: absolute;
    left: 362px;
    top: 312px;
    width: 476px;
    height: 576px;
    background: var(--label);
    overflow: hidden;
  }
  .sprig {
    position: absolute;
  }
  .sprig--left {
    left: 0;
    top: 126px;
    width: 146px;
    height: 298px;
    background: linear-gradient(160deg, rgba(195,198,205,0.0) 0%, rgba(195,198,205,0.55) 40%, rgba(195,198,205,0.35) 100%);
    border-radius: 0 70% 0 0;
  }
  .sprig--right {
    left: 284px;
    top: 0;
    width: 192px;
    height: 264px;
    background: linear-gradient(200deg, rgba(230,231,233,0.9) 0%, rgba(230,231,233,0.6) 60%, rgba(230,231,233,0.0) 100%);
    border-radius: 0 0 0 70%;
  }
  .brand-seal {
    position: absolute;
    left: 108px;
    top: 158px;
    width: 260px;
    height: 260px;
    border-radius: 50%;
    background: var(--slate);
    display: flex;
    align-items: center;
    justify-content: center;
  }
  .brand-name {
    font-family: "Josefin Sans", sans-serif;
    font-weight: 300;
    font-size: 36px;
    letter-spacing: 5px;
    color: var(--label);
  }
  .product-copy {
    position: absolute;
    left: 0;
    right: 0;
    top: 466px;
    text-align: center;
    font-family: "Tinos", serif;
    font-variant: small-caps;
  }
  .product-copy__claims {
    margin: 0;
    font-size: 16px;
    line-height: 18.5px;
    color: var(--copy-grey);
  }
  .product-copy__volume {
    margin: 8px 0 0;
    font-size: 24px;
    color: var(--copy-dark);
  }
</style>
</head>
<body>
  <main class="label">
    <div class="sprig sprig--left" role="img" aria-label="Grey leafy fern sprig decoration"></div>
    <div class="sprig sprig--right" role="img" aria-label="Pale grey leafy fern sprig decoration"></div>

    <div class="brand-seal">
      <span class="brand-name">lumavale</span>
    </div>

    <section class="product-copy">
      <p class="product-copy__claims">
        Formulated by a Naturopath,<br>
        Anti-aging Therapy, Organic Facial Oil,<br>
        with CoEnzyme Q10 and Rosehip Seed Oil
      </p>
      <p class="product-copy__volume">100ml e3.38fl.oz.</p>
    </section>
  </main>
</body>
</html>
```